Website for a financial survey consultancy

WHO WE ARE
We're a niche HR consultancy specialising in salary comparison surveys for the financial asset management industry. We position ourselves as a small, highly responsive organisation with a strong personal relationship with each of our 50+ blue-chip clients.

WHAT WE DO
Our business is 80% surveys (= products), 20% consultancy (= services). The surveys are a set of online products which clients interact with to find the information they are interested in.

WHAT WE WANT
We are completely revising our existing marketing website and need a new up-to-date look and feel for the site. We want you to design 2 web pages
- Home page
- Internal content page

More details below in Must Have Priorities.

REFERENCE SITES
- www.tallowmere.com - nice background image
- www.quimbelt.com - ignoring the animations
- www.palvastro.com
- www.dulmiko.com - clean, fresh, styly but prob not corporate enough
- www.orvettagrove.com - spacious, beautiful, slightly dated tho
- www.plinzer.co.uk - ignore the colours. Like the simplicity, larger font size (although want to stick with sans-serif fonts for main content)

DELIVERABLES
The final designs should be delivered as one or more PSD files with clearly named layers. All design elements and treatments should be separated out, for example use adjustment layers rather than applied (and subsequently irreversible) adjustments, strokes, shading, etc.

WHAT NEXT
I'll be monitoring the contest every day and can respond to questions fast. You can IM me on Skype or MSN.

Reason: Hi folks,

I am extending the deadline to this project as I am travelling this week and therefore will not be able to make a final decision until next Monday. I will try and provide further feedback over the course of this week but I am only going to be online occasionally so be prepared to wait a few days for a reply from me.

Thanks for all the designs so far.

Owen

Target Market(s)

In order of importance, most important first

1. Potential customers - UK & US financial industry HR professionals, short on time. Heard about us already, want to find out more about what we do, confirm relevance for their needs. Core goal - establish credibility: are we properly resourced, will we be around for years to come, are we *real*.

2. Existing customers - UK & US financial industry professionals, short on time, under pressure, want results quickly, minimum faff, expect high quality, slickly presented information. Primary action: login and use surveys.

3. Industry professionals/researchers - probably arriving through blog content, looking to browse and hoover information. Valuable for their ability to spread awareness of who we are amongst their peers.

Industry/Entity Type

Financial

Requirements
Must have
• GENERAL
Style cues - Corporate, professional, financial, stylish, slick, clean, spacious, light
Size - standard 960px grid

NAVIGATION
- [ Home | About us | Surveys | Consulting | Blog ]
- Sub-nav (roll-over dropdown) on About Us, Surveys & Consulting

ALL PAGES
- Site navigation
- Client login (on screen permanently or link to ajaxy in-page pop-up)
- Footer section
- Existing logo (attached)* - this is obviously an important reference point in the design, esp colour

HOME PAGE
- Communicate (link thru to?) survey/consulting split
- Large photo(s)/backdrop (2-3 interchangeable options ideally). Please consider what rights agreement will be necessary for any photos you include in your design.
- Possibly bigger more prominent version of logo
- Strap line/sentence - "Focussed data is the key to success"
- 3 recent blog posts (should look good with and without blog post images)
- Free downloadable PDF research report + supporting blurb

INTERNAL PAGE
- Page title
- Content - typical page will be less than one screenfull
- Level 1 sub-heading
- Level 2 sub-heading
- Bulleted list
- Content supporting image (any image will do - interested in placement, borders (if any), spacing, caption, etc)
- 'Do something' button

* Note: there is some internal debate about this logo at the moment. Some (me) are keen for it to change, some (not me!) are not. If you have an web page design idea/concept that requires an evolution of the logo, go ahead and evolve it. We can explore this further in the design process as necessary, but don't sweat it.
Nice to have
• Values to communicate
- Knowledgeable
- Professional
- Secure
- Personal
- Experienced
- Financial industry specific
- Accurate
- Reliable
Should not have
• - Search box
- Social media links, other than RSS feed button (discrete)

```html
<!DOCTYPE html>
<html lang="en">
<head>
<meta charset="utf-8">
<title>Norvane – HR consultancy</title>
<link rel="stylesheet" href="https://fonts.googleapis.com/css2?family=Archivo+Narrow:wght@400;500&family=Arimo:wght@400;700&family=PT+Sans:wght@400;700&display=swap">
<style>
:root{
  --stage:#333333;
  --brand:#650c0c;
  --brand-text:#6a0e0e;
  --nav-top:#4a4a4a;
  --nav-bottom:#2e2e2e;
  --login-bg:#e2cbb0;
  --ink:#111111;
  --body-ink:#222222;
  --blog-ink:#2f2f2f;
  --accent:#e2561b;
  --footer-bg:#040a10;
  --footer-ink:#d0d0d0;
  --footer-muted:#9a9a9a;
  --sky-top:#c9d6ea;
  --sky-mid:#eef1f6;
  --bridge:#f6f2ea;
}
*{margin:0;padding:0;box-sizing:border-box}
html,body{width:1200px;height:900px;overflow:hidden;background:var(--stage)}
body{position:relative;font-family:"Arimo",Arial,sans-serif}
.site{position:absolute;left:121px;top:69px;width:964px;height:757px;overflow:hidden}
.hero-photo{position:absolute;left:0;top:0;width:964px;height:674px;
  background:linear-gradient(115deg,var(--sky-top) 0%,var(--sky-mid) 30%,var(--bridge) 55%,#e9e4da 75%,var(--sky-top) 100%)}
.side-veil{position:absolute;left:670px;top:0;width:261px;height:674px;background:rgba(255,255,255,.55)}
.brand{position:absolute;left:28px;top:36px}
.brand-square{width:86px;height:84px;background:var(--brand)}
.brand-name{margin-top:8px;font-size:22px;color:var(--brand);font-weight:400;letter-spacing:.5px}
.main-nav{position:absolute;left:475px;top:92px;width:477px;height:48px;
  background:linear-gradient(var(--nav-top),var(--nav-bottom));display:flex;align-items:center;
  padding-left:27px;font-family:"PT Sans",Tahoma,sans-serif;font-size:12px;color:#fff;text-transform:uppercase}
.main-nav a{color:#fff;text-decoration:none}
.main-nav .sep{margin:0 23px}
.intro{position:absolute;left:25px;top:258px;width:443px;height:302px;background:rgba(255,255,255,.93);padding:14px 22px 0 18px}
.intro h1{font-family:"Archivo Narrow",Arial,sans-serif;font-weight:400;font-size:68px;line-height:72px;color:var(--ink);letter-spacing:-1px}
.intro .strap{margin-top:4px;font-family:"Archivo Narrow",Arial,sans-serif;font-size:22px;line-height:29px;color:var(--brand-text);font-weight:500}
.intro p{margin:14px 0 0 6px;font-size:12.5px;line-height:15.5px;color:var(--body-ink);text-align:justify}
.login{position:absolute;left:678px;top:146px;width:247px;height:179px;background:var(--login-bg);padding:14px 8px;
  font-family:"PT Sans",Tahoma,sans-serif}
.login h2{font-family:"Arimo",Arial,sans-serif;font-size:14px;color:var(--brand);font-weight:700}
.login label{display:block;font-size:12px;color:#222;margin-top:6px}
.login .field{display:block;width:225px;height:22px;background:#fff;border:0;margin-top:3px}
.login-actions{display:flex;align-items:center;margin-top:12px}
.login-btn{width:72px;height:25px;border:1px solid #c8c8c8;border-radius:5px;background:linear-gradient(#fff,#ececec);
  font-family:"PT Sans",Tahoma,sans-serif;font-size:12px;color:#222}
.forgot{margin-left:4px;font-size:11px;font-weight:700;color:#111}
.blogs{position:absolute;left:685px;top:356px;width:240px}
.blogs h2{font-family:"Archivo Narrow",Arial,sans-serif;font-weight:400;font-size:21px;color:var(--ink);margin-left:3px}
.post{display:flex;margin-top:14px;height:70px}
.post + .post{margin-top:12px}
.post-thumb{width:53px;height:53px;border:3px solid #9a9a9a;background:linear-gradient(#cfd3d8,#a9aeb5);flex:none}
.post-body{margin-left:7px}
.post-body p{font-family:"PT Sans",Tahoma,sans-serif;font-size:11px;line-height:13px;font-weight:700;color:var(--blog-ink)}
.read-more{display:inline-block;margin:6px 0 0 2px;font-size:10.5px;color:#111;text-decoration:underline;font-family:"PT Sans",Tahoma,sans-serif}
.read-more span{color:var(--accent);text-decoration:none;font-weight:700;margin-left:3px}
.site-footer{position:absolute;left:0;top:674px;width:964px;height:83px;background:var(--footer-bg)}
.footer-nav{position:absolute;left:24px;top:26px;font-family:"PT Sans",Tahoma,sans-serif;font-size:12px;color:var(--footer-ink)}
.footer-nav .sep{margin:0 24px}
.copyright{position:absolute;left:24px;top:44px;font-family:"PT Sans",Tahoma,sans-serif;font-size:10px;color:var(--footer-muted)}
.footer-brand{position:absolute;left:894px;top:4px;width:37px}
.footer-brand .brand-square{width:37px;height:37px;background:#e6e6e6}
.footer-brand .brand-name{margin-top:3px;font-size:9px;color:#e6e6e6;letter-spacing:0}
</style>
</head>
<body>
<div class="site">
  <div class="hero-photo" role="img" aria-label="Photograph of a white arched cable bridge against a pale cloudy sky"></div>
  <div class="side-veil"></div>

  <div class="brand">
    <div class="brand-square"></div>
    <div class="brand-name">Norvane</div>
  </div>

  <nav class="main-nav">
    <a href="#">Home</a><span class="sep">|</span>
    <a href="#">About us</a><span class="sep">|</span>
    <a href="#">Surveys</a><span class="sep">|</span>
    <a href="#">Consulting</a><span class="sep">|</span>
    <a href="#">Blog</a>
  </nav>

  <section class="intro">
    <h1>HR consultancy</h1>
    <p class="strap">specialising in salary comparison surveys for the financial asset management industry</p>
    <p>Lorem ipsum dolor sit amet, consectetur adipiscing elit. Cras ante dui, viverra non vehicula in, condimentum id ipsum. Fusce at arcu metus. Fusce eu justo nisl. Maecenas consequat condimentum ante, quis tincidunt neque viverra sed. Aenean tempus rhoncus dolor, at dapibus ipsum dapibus at. Nulla ac turpis a quam venenatis molestie sit amet ut enim. Sed elementum feugiat bibendum. Morbi sed adipiscing tellus.</p>
  </section>

  <form class="login">
    <h2>Client LOGIN</h2>
    <label>User Name</label>
    <span class="field"></span>
    <label>Password</label>
    <span class="field"></span>
    <div class="login-actions">
      <button class="login-btn" type="button">LOGIN ››</button>
      <span class="forgot">Forgot Password?</span>
    </div>
  </form>

  <section class="blogs">
    <h2>Latest Blogs</h2>
    <article class="post">
      <div class="post-thumb" role="img" aria-label="Author portrait"></div>
      <div class="post-body">
        <p>Lorem ipsum dolor sit amet, consectetur adipiscing elit. Cras ante du</p>
        <a class="read-more" href="#">Read More</a><span class="read-more"><span>»</span></span>
      </div>
    </article>
    <article class="post">
      <div class="post-thumb" role="img" aria-label="Author portrait"></div>
      <div class="post-body">
        <p>Lorem ipsum dolor sit amet, consectetur adipiscing elit. Cras ante du</p>
        <a class="read-more" href="#">Read More</a><span class="read-more"><span>»</span></span>
      </div>
    </article>
    <article class="post">
      <div class="post-thumb" role="img" aria-label="Author portrait"></div>
      <div class="post-body">
        <p>Lorem ipsum dolor sit amet, consectetur adipiscing elit. Cras ante du</p>
        <a class="read-more" href="#" style="margin-top:0">Read More</a><span class="read-more" style="margin-top:0"><span>»</span></span>
      </div>
    </article>
  </section>

  <footer class="site-footer">
    <div class="footer-nav">Home<span class="sep">|</span>about us<span class="sep">|</span>Surveys<span class="sep">|</span>Consulting<span class="sep">|</span>Blog</div>
    <div class="copyright">© 2011 Norvane. All rights reserved</div>
    <div class="footer-brand">
      <div class="brand-square"></div>
      <div class="brand-name">Norvane</div>
    </div>
  </footer>
</div>
</body>
</html>
```